Hi we have a company called Brenlock Protection Services and are looking for a new design we are wanting flames as the last card was great with the whole background flames but you cant really see the services offered, phone, names etc.

We need something more upmarket and professional and only have a small budget

We need the words Brenlock Protection Services, Martin Pevelle MAQSrT - Fire Safety Consultant, Phone No 0492365140 address : PO Box 8362 TWRL 4183 ABN 71836205947, NRTW Lic.5742816 Email martin@brenlockgroup.com.au

Industry/Entity Type

Fire Safety

Font styles to use
Sans Serif

Colors
ec2027
ffc214

```html
<!DOCTYPE html>
<html lang="en">
<head>
<meta charset="utf-8">
<title>Brenlock Protection Services – Business Card</title>
<link rel="stylesheet" href="https://fonts.googleapis.com/css2?family=Arimo:wght@700&display=swap">
<style>
  :root {
    --paper: #ffffff;
    --ink: #000000;
    --gold: #f7c21a;
    --contact-orange: #f04c1c;
    --panel-dark: #9a1c14;
    --panel-light: #f7d23e;
  }
  html, body {
    margin: 0;
    padding: 0;
    overflow: hidden;
    background: var(--paper);
  }
  .card {
    position: relative;
    width: 1200px;
    height: 880px;
    background: var(--paper);
    font-family: "Arimo", Arial, Helvetica, sans-serif;
    font-weight: 700;
    overflow: hidden;
  }
  .photo-panel {
    position: absolute;
    left: 0;
    top: 0;
    width: 478px;
    height: 880px;
    background: linear-gradient(to bottom, var(--panel-dark) 0%, var(--panel-light) 100%);
  }
  .details {
    position: absolute;
    left: 478px;
    right: 0;
    top: 0;
    bottom: 0;
    text-align: center;
  }
  .details > * {
    position: absolute;
    left: 0;
    right: 0;
    margin: 0;
    white-space: nowrap;
  }
  .company-name {
    top: 0;
    font-size: 70px;
    line-height: 95px;
    color: var(--ink);
    letter-spacing: -0.5px;
  }
  .person-name {
    top: 220px;
    font-size: 50px;
    line-height: 56px;
    color: var(--gold);
  }
  .person-role {
    top: 307px;
    font-size: 42px;
    line-height: 48px;
    color: var(--gold);
  }
  .contact {
    top: 439px;
    font-size: 44px;
    line-height: 57px;
    color: var(--contact-orange);
  }
  .email {
    top: 802px;
    font-size: 35px;
    line-height: 48px;
    color: var(--contact-orange);
  }
</style>
</head>
<body>
  <div class="card">
    <div class="photo-panel" role="img" aria-label="Photograph of bright yellow and orange flames fading to deep red"></div>
    <div class="details">
      <h1 class="company-name">Brenlock Protection<br>Services</h1>
      <p class="person-name">Martin Pevelle</p>
      <p class="person-role">MAQSrT - Fire Safety Consultant</p>
      <p class="contact">Phone No: 0492365140<br>Address : PO Box 8362,<br>TWRL 4183 ABN 71836205947<br>NRTW Lic.5742816</p>
      <p class="email">Email: martin@brenlockgroup.com.au</p>
    </div>
  </div>
</body>
</html>
```